Velmira website

A clean uncluttered design that shows at glance that we are in the Media and design and publishing business.

We would like to see designs that use colours that show warmth and quality.

The website should show:
- products
- projects

These should be displaxed in spaces that we can add or interchanges with new products or projects.

Target Market(s)

Business and project managers and buyers and authors.

Industry/Entity Type

Business

Requirements
Must have
• Good colours. Not too strong, not weak, but reflecting quality.

```html
<!DOCTYPE html>
<html lang="en">
<head>
<meta charset="utf-8">
<title>Velmira Media</title>
<link href="https://fonts.googleapis.com/css2?family=Open+Sans:wght@300;400;600;700;800&display=swap" rel="stylesheet">
<style>
:root{
  --teal:#27aeb7;
  --slate:#6b6f7a;
  --slate-dark:#5d616b;
  --slate-mid:#7f8a99;
  --slate-light:#a3a9b3;
  --tab-active:#dde2e8;
  --panel-bg:#f3f6f9;
  --text:#555a63;
  --text-dark:#3e424a;
  --rule:#d9dbdf;
  --white:#fff;
}
*{box-sizing:border-box;margin:0;padding:0}
html,body{width:990px;height:1200px;overflow:hidden;background:var(--white)}
body{position:relative;font-family:"Open Sans",Arial,sans-serif;color:var(--text);font-size:8px;line-height:1.3}
.abs{position:absolute}
a{color:inherit;text-decoration:none}

/* header */
.brand{left:133px;top:14px}
.brand-name{font-size:31px;font-weight:800;color:var(--teal);letter-spacing:-.5px;line-height:1}
.brand-tag{position:absolute;left:67px;top:31px;font-size:12px;font-weight:700;color:var(--slate-light);letter-spacing:.5px}
.social-top{left:645px;top:32px;display:flex;gap:10px}
.social-top span,.social-foot span{width:9px;height:9px;border-radius:50%;background:var(--slate);display:block}
.sep{left:760px;top:31px;width:1px;height:10px;background:var(--rule)}
.top-links{left:778px;top:31px;display:flex;gap:9px;font-size:7.5px;color:var(--text)}

/* nav */
.nav{left:133px;top:74px;width:724px;height:37px;background:var(--slate);box-shadow:0 10px 8px -6px rgba(0,0,0,.25)}
.nav-home{position:absolute;left:0;top:0;width:36px;height:37px;background:var(--slate-dark);display:flex;align-items:center;justify-content:center}
.nav-links{position:absolute;top:0;left:0;height:37px;width:100%}
.nav-links a{position:absolute;top:13px;font-size:8.5px;color:var(--white)}
.nav-search{position:absolute;right:0;top:0;width:38px;height:37px;background:var(--teal);display:flex;align-items:center;justify-content:center}

/* hero */
.hero-photo{left:133px;top:130px;width:538px;height:309px;background:linear-gradient(110deg,#d9e2ea 0%,#b9c7d4 35%,#8fa2b5 60%,#dfe7ee 100%)}
.feature-panel{color:var(--white);padding:22px 18px 0}
.feature-title{font-size:14.5px;font-weight:300;line-height:1.2;letter-spacing:-.2px}
.feature-title b{display:block;font-weight:700;font-size:14.5px}
.feature-text{margin-top:9px;font-size:7.6px;line-height:1.35}
.hero-panel{left:671px;top:130px;width:186px;height:309px;background:var(--slate-mid)}
.btn{display:inline-flex;align-items:center;gap:8px;background:var(--teal);color:var(--white);font-size:7px;font-weight:700;padding:0 9px;height:24px}
.hero-panel .btn{margin-top:17px;padding:0 9px 0 12px}

/* cards */
.card-photo{top:458px;width:167px;height:148px}
.card-panel{top:458px;width:186px;height:148px}
.photo-meet{left:133px;background:linear-gradient(135deg,#e6ebef,#9aa5b1 55%,#3b4656)}
.panel-marketing{left:300px;background:var(--slate-light)}
.photo-office{left:504px;background:linear-gradient(135deg,#cfd7df,#e8ecef 50%,#7a828d)}
.panel-branding{left:671px;background:var(--slate)}

/* projects tabs */
.projects{left:133px;top:625px;width:353px;height:226px;background:var(--panel-bg)}
.tabs{display:flex;height:44px;background:var(--slate-light)}
.tab{flex:1;display:flex;align-items:center;justify-content:center}
.tab.active{background:var(--tab-active)}
.projects-body{padding:16px 17px}
.section-title{font-size:14px;font-weight:300;color:var(--text-dark);letter-spacing:-.2px}
.projects-body p{font-size:7.6px;margin-top:7px;line-height:1.35}
.projects-body p+p{margin-top:10px}

/* products */
.col-head{display:flex;justify-content:space-between;align-items:center}
.dots{display:flex;gap:2px}
.dots i{width:5px;height:5px;border-radius:50%;background:var(--slate-light);display:block}
.dots i:last-child{background:var(--teal)}
.products{left:504px;top:622px;width:167px}
.product{display:flex;gap:7px;padding:5px 0 6px;border-bottom:1px solid var(--rule);height:43px}
.product:last-child{border-bottom:0}
.product .thumb{width:30px;height:30px;flex:none;background:linear-gradient(135deg,#e3e8ed,#8d98a6)}
.product h4{font-size:7px;font-weight:600;color:var(--teal)}
.product p{font-size:6.6px;line-height:1.3;margin-top:1px}
.products-list{margin-top:10px}
.products .btn{position:absolute;left:97px;top:205px;width:70px;height:24px}
.works{left:690px;top:622px;width:167px}
.section-title.bold{font-weight:700}
.work-photo{left:690px;width:167px}
.work-team{top:654px;height:62px;background:linear-gradient(180deg,#f1f3f5,#c4ccd5 60%,#e9ecef)}
.work-highlight{left:690px;top:723px;width:167px;height:61px;background:var(--teal);color:var(--white);text-align:center;font-size:7px;font-weight:700;padding-top:18px}
.work-meeting{top:790px;height:62px;background:linear-gradient(135deg,#dfe5eb,#7f8b99 60%,#2f3846)}

/* news */
.news{top:869px;width:106px}
.news-date{font-size:14px;color:var(--text-dark);padding-bottom:3px;border-bottom:3px solid var(--rule)}
.news-date small{font-size:8px;font-weight:600}
.news h5{margin-top:12px;font-size:7.6px;font-weight:700;color:var(--text-dark)}
.news p{font-size:6.6px;line-height:1.3;margin-top:1px}
.news a{font-size:6.6px;font-weight:700;color:var(--teal);display:block;margin-top:2px}

/* tweet band */
.tweet-band{left:0;top:1035px;width:990px;height:24px;background:var(--teal);color:var(--white);font-size:7.5px}
.tweet-band .bird{position:absolute;left:133px;top:6px;width:12px;height:12px;border-radius:50%;background:var(--white)}
.tweet-band p{position:absolute;left:159px;top:6px}
.tweet-arrows{position:absolute;left:809px;top:0;display:flex}
.tweet-arrows span{width:24px;height:24px;display:flex;align-items:center;justify-content:center}
.tweet-arrows span+span{background:#1f9ba3}

/* footer */
.footer{left:0;top:1059px;width:990px;height:117px;background:var(--slate)}
.footer h3{position:absolute;left:133px;top:37px;font-size:14px;font-weight:700;color:var(--white);line-height:1}
.footer .lead{position:absolute;left:133px;top:51px;font-size:6.6px;color:var(--white)}
.social-foot{position:absolute;left:133px;top:70px;display:flex;gap:13px}
.social-foot span{width:12px;height:12px;background:var(--white)}
.footer-links{position:absolute;right:133px;top:54px;display:flex;gap:18px;font-size:7px;color:var(--white)}
.copyright{left:0;top:1176px;width:990px;height:24px;background:var(--slate-dark);color:var(--white);font-size:6.6px;padding:10px 0 0 133px}
</style>
</head>
<body>

<header>
  <div class="abs brand">
    <div class="brand-name">Velmira</div>
    <div class="brand-tag">MEDIA</div>
  </div>
  <div class="abs social-top" aria-label="Social links"><span></span><span></span><span></span><span></span><span></span></div>
  <div class="abs sep"></div>
  <nav class="abs top-links"><a>News</a><a>FAQ</a><a>Contact</a></nav>
</header>

<nav class="abs nav">
  <div class="nav-home">
    <svg width="13" height="12" viewBox="0 0 13 12"><path d="M6.5 1 L12 6 H10.5 V11 H7.8 V7.8 H5.2 V11 H2.5 V6 H1 Z" fill="#fff"/></svg>
  </div>
  <div class="nav-links">
    <a style="left:62px">About</a><a style="left:114px">Portfolio</a><a style="left:174px">Blog</a><a style="left:220px">Shortcodes</a><a style="left:293px">Features</a><a style="left:356px">Pages</a><a style="left:409px">Contact</a>
  </div>
  <div class="nav-search">
    <svg width="12" height="12" viewBox="0 0 12 12"><circle cx="5" cy="5" r="3.5" fill="none" stroke="#fff" stroke-width="1.6"/><path d="M7.6 7.6 L11 11" stroke="#fff" stroke-width="1.8"/></svg>
  </div>
</nav>

<div class="abs hero-photo" role="img" aria-label="Smiling businessman with arms crossed in a bright office, colleagues blurred behind"></div>
<section class="abs hero-panel feature-panel">
  <h2 class="feature-title">RESPONSIVE DESIGN<b>BUY NOW</b></h2>
  <p class="feature-text">Lorem ipsum dolor sit amet, consectetur adipisicing elit, sed do eiusmod tempor incididunt ut labore et dolore magna aliqua.</p>
  <a class="btn">ALL POST <svg width="8" height="8" viewBox="0 0 8 8"><path d="M4 0V8M0 4H8" stroke="#fff" stroke-width="2"/></svg></a>
</section>

<div class="abs card-photo photo-meet" role="img" aria-label="Business people shaking hands across a meeting table"></div>
<section class="abs card-panel panel-marketing feature-panel">
  <h2 class="feature-title">MARKETING SORS<b>START NOW</b></h2>
  <p class="feature-text">Lorem ipsum dolor sit amet, consectetur adipisicing elit, sed do eiusmod tempor incididunt ut labore et dolore magna aliqua.</p>
</section>
<div class="abs card-photo photo-office" role="img" aria-label="Two colleagues working at a laptop, one on the phone"></div>
<section class="abs card-panel panel-branding feature-panel">
  <h2 class="feature-title">BRANDING<b>START NOW</b></h2>
  <p class="feature-text">Lorem ipsum dolor sit amet, consectetur adipisicing elit, sed do eiusmod tempor incididunt ut labore et dolore magna aliqua.</p>
</section>

<section class="abs projects">
  <div class="tabs">
    <div class="tab"><svg width="20" height="16" viewBox="0 0 20 16" fill="#fff"><rect x="1" y="10" width="3" height="6"/><rect x="6" y="8" width="3" height="8"/><rect x="11" y="9" width="3" height="7"/><rect x="16" y="5" width="3" height="11"/><path d="M1 8 L7 4 L11 6 L18 1" stroke="#fff" stroke-width="1.5" fill="none"/></svg></div>
    <div class="tab"><svg width="20" height="15" viewBox="0 0 20 15"><rect x="3" y="1" width="14" height="10" fill="none" stroke="#fff" stroke-width="1.5"/><rect x="0" y="12" width="20" height="2" fill="#fff"/></svg></div>
    <div class="tab active"><svg width="16" height="16" viewBox="0 0 16 16" stroke="#6b6f7a" stroke-width="1.4" fill="none"><path d="M1 5V1H5M1 1L5.5 5.5M11 1H15V5M15 1L10.5 5.5M1 11V15H5M1 15L5.5 10.5M15 11V15H11M15 15L10.5 10.5"/></svg></div>
    <div class="tab"><svg width="18" height="18" viewBox="0 0 18 18" fill="none" stroke="#fff" stroke-width="1.4"><path d="M1 8 Q9 -2 17 8 Q13 6 9 8 Q5 6 1 8Z" fill="#fff"/><path d="M9 8V15 Q9 17 7 16"/></svg></div>
    <div class="tab"><svg width="22" height="18" viewBox="0 0 22 18" fill="#fff"><ellipse cx="8" cy="10" rx="7" ry="6"/><path d="M3 14 L2 18 L7 15Z"/><ellipse cx="16" cy="6" rx="5" ry="4.5" stroke="#a3a9b3" stroke-width="1"/></svg></div>
  </div>
  <div class="projects-body">
    <h2 class="section-title">PROJECTS</h2>
    <p>Lorem ipsum dolor sit amet, consectetur adipisicing elit, sed do eiusmod tempor incididunt ut labore et dolore magna aliqua. Ut enim ad minim veniam, quis nostrud exercitation ullamco laboris .</p>
    <p>At vero eos et accusamus et iusto odio dignissimos ducimus qui blanditiis praesentium voluptatum deleniti atque corrupti quos dolores et quas molestias excepturi sint occaecati cupiditate non provident, similique sunt in culpa qui officia deserunt mollitia distinctio.  Nam libero tempore, cum soluta nobis est eligendi optio voluptas assumenda est, omnis dolor repellendus.</p>
  </div>
</section>

<section class="abs products">
  <div class="col-head"><h2 class="section-title">LATEST PRODUCTS</h2><div class="dots"><i></i><i></i><i></i></div></div>
  <div class="products-list">
    <div class="product"><div class="thumb" role="img" aria-label="Product thumbnail"></div><div><h4>Company Aurelence</h4><p>Lorem ipsum dolor sit amet, consectetur adipisicing elit, sed do.</p></div></div>
    <div class="product"><div class="thumb" role="img" aria-label="Product thumbnail"></div><div><h4>Stock Runing</h4><p>Lorem ipsum dolor sit amet, consectetur adipisicing elit, sed do.</p></div></div>
    <div class="product"><div class="thumb" role="img" aria-label="Product thumbnail"></div><div><h4>Amber Shines Reborn</h4><p>Lorem ipsum dolor sit amet, consectetur adipisicing elit, sed do.</p></div></div>
    <div class="product"><div class="thumb" role="img" aria-label="Product thumbnail"></div><div><h4>My protest Paid</h4><p>Lorem ipsum dolor sit amet, consectetur adipisicing elit, sed do.</p></div></div>
  </div>
  <a class="btn">ALL POST <svg width="8" height="8" viewBox="0 0 8 8"><path d="M4 0V8M0 4H8" stroke="#fff" stroke-width="2"/></svg></a>
</section>

<section class="abs works">
  <div class="col-head"><h2 class="section-title bold">RECENT WORKS</h2><div class="dots"><i></i><i></i><i></i></div></div>
</section>
<div class="abs work-photo work-team" role="img" aria-label="Team of smiling business people standing together"></div>
<div class="abs work-highlight">CORVELA THEME<br><svg width="8" height="8" viewBox="0 0 8 8" style="margin-top:5px"><path d="M4 0V8M0 4H8" stroke="#fff" stroke-width="2"/></svg></div>
<div class="abs work-photo work-meeting" role="img" aria-label="Colleagues in a meeting around a table"></div>

<article class="abs news" style="left:133px"><div class="news-date">29 <small>MAY</small></div><h5>GOOD IDEA</h5><p>Duis aute irure dolor inserar reprehenderit in voluptate velit esse cillum dolore eu fugiat pariatur relased.</p><a>read more</a></article>
<article class="abs news" style="left:257px"><div class="news-date">28 <small>MAY</small></div><h5>AVASOME DESIGN</h5><p>Duis aute irure dolor inserar reprehenderit in voluptate velit esse cillum dolore eu fugiat pariatur relased.</p><a>read more</a></article>
<article class="abs news" style="left:380px"><div class="news-date">27 <small>MAY</small></div><h5>PERFECT PIXELS</h5><p>Duis aute irure dolor inserar reprehenderit in voluptate velit esse cillum dolore eu fugiat pariatur relased.</p><a>read more</a></article>
<article class="abs news" style="left:504px"><div class="news-date">26 <small>MAY</small></div><h5>UNIQUE COLURS</h5><p>Duis aute irure dolor inserar reprehenderit in voluptate velit esse cillum dolore eu fugiat pariatur relased.</p><a>read more</a></article>
<article class="abs news" style="left:628px"><div class="news-date">25 <small>MAY</small></div><h5>EASY EDITABLE</h5><p>Duis aute irure dolor inserar reprehenderit in voluptate velit esse cillum dolore eu fugiat pariatur relased.</p><a>read more</a></article>
<article class="abs news" style="left:751px"><div class="news-date">24 <small>MAY</small></div><h5>LAYERED PSD</h5><p>Duis aute irure dolor inserar reprehenderit in voluptate velit esse cillum dolore eu fugiat pariatur relased.</p><a>read more</a></article>

<div class="abs tweet-band">
  <span class="bird"></span>
  <p>Nam libero tempore, cum soluta nobis est eligendi optio cumque nihil impedit quo minus id quod maxime placeat facere possimus, omnis voluptas <b>@lumenpress</b></p>
  <div class="tweet-arrows">
    <span><svg width="5" height="7" viewBox="0 0 5 7"><path d="M4 0.5 L1 3.5 L4 6.5" stroke="#fff" stroke-width="1.4" fill="none"/></svg></span>
    <span><svg width="5" height="7" viewBox="0 0 5 7"><path d="M1 0.5 L4 3.5 L1 6.5" stroke="#fff" stroke-width="1.4" fill="none"/></svg></span>
  </div>
</div>

<footer class="abs footer">
  <h3>GET IN TOUCH</h3>
  <p class="lead">Lorem ipsum dolor sit amet, consectetur adipisicing</p>
  <div class="social-foot" aria-label="Social links"><span></span><span></span><span></span><span></span><span></span><span></span></div>
  <nav class="footer-links"><a>Home</a><a>Pages</a><a>Portfolio</a><a>Shortcodes</a><a>Features</a><a>Blog</a><a>Contact</a></nav>
</footer>
<div class="abs copyright">Copyright 2013 Northfold Studio</div>

</body>
</html>
```